Brightwell Holdings -Business Card Design Project

I have a new logo to put onto business cards - attached
The word doc shows how I want it all laid out - front page and rear
The lettering I want is clean and rounded - modern
Updates
Project Deadline Extended
Reason: There was no original deadline!
Target Market(s)
25-49 year old leaders and entrepreneurs in Australia
Industry/Entity Type
Business

```html
<!DOCTYPE html>
<html lang="en">
<head>
<meta charset="utf-8">
<title>Brightwell Holdings – Business Card</title>
<link rel="stylesheet" href="https://fonts.googleapis.com/css2?family=Open+Sans:wght@400;600;700&display=swap">
<style>
  :root {
    --backdrop: #e4e5e7;
    --card: #fbfbfb;
    --brand-blue: #0b57a4;
    --band-dark: #333537;
    --text-grey: #3a3a3a;
  }
  * { margin: 0; padding: 0; box-sizing: border-box; }
  html, body {
    width: 1200px; height: 900px; overflow: hidden;
    background: var(--backdrop);
    font-family: "Open Sans", Arial, sans-serif;
  }
  .canvas {
    position: relative; width: 1200px; height: 900px;
    display: flex; align-items: center; justify-content: center;
  }
  .business-card {
    position: relative; width: 1050px; height: 600px;
    background: var(--card);
    box-shadow: 0 6px 22px rgba(0,0,0,0.12);
    overflow: hidden;
  }
  .corner-swoosh { position: absolute; inset: 0; width: 100%; height: 100%; }
  .holder-block { position: absolute; left: 72px; top: 112px; }
  .holder-name {
    color: var(--brand-blue); font-weight: 700; font-size: 27px;
    letter-spacing: 0.5px; line-height: 1.15;
  }
  .holder-title { color: var(--text-grey); font-size: 23px; line-height: 1.25; }
  .address {
    position: absolute; left: 72px; top: 258px;
    color: var(--text-grey); font-size: 22px; line-height: 1.4;
  }
  .contact-list {
    position: absolute; left: 72px; top: 420px; list-style: none;
    color: var(--text-grey); font-size: 22px; line-height: 1.45;
  }
  .contact-list li { display: flex; align-items: center; gap: 14px; }
  .contact-icon { width: 18px; height: 18px; fill: var(--brand-blue); flex: none; }
  .brand-lockup {
    position: absolute; left: 470px; top: 190px;
    display: flex; align-items: center; gap: 16px;
  }
  .brand-mark { width: 22px; height: 22px; background: var(--brand-blue); flex: none; }
  .brand-name {
    color: var(--brand-blue); font-weight: 600; font-size: 38px;
    line-height: 1; white-space: nowrap;
  }
</style>
</head>
<body>
<main class="canvas">
  <section class="business-card" aria-label="Business card front">
    <svg class="corner-swoosh" viewBox="0 0 1050 600" aria-hidden="true">
      <path d="M700 0 Q1005 200 1050 570 L1050 0 Z" fill="var(--band-dark)"/>
      <path d="M724 0 Q1016 180 1050 500 L1050 0 Z" fill="var(--card)"/>
      <path d="M732 0 Q1020 170 1050 478 L1050 0 Z" fill="var(--brand-blue)"/>
    </svg>

    <div class="holder-block">
      <p class="holder-name">DANIEL HARTLEY</p>
      <p class="holder-title">Managing Director</p>
    </div>

    <p class="address">Level 9, 27 Harbour Street<br>Sydney NSW</p>

    <ul class="contact-list">
      <li>
        <svg class="contact-icon" viewBox="0 0 24 24"><path d="M6.6 10.8a15.1 15.1 0 0 0 6.6 6.6l2.2-2.2a1 1 0 0 1 1-.25 11.4 11.4 0 0 0 3.6.57 1 1 0 0 1 1 1V20a1 1 0 0 1-1 1A17 17 0 0 1 3 4a1 1 0 0 1 1-1h3.5a1 1 0 0 1 1 1c0 1.25.2 2.45.57 3.57a1 1 0 0 1-.25 1z"/></svg>
        02 5550 1427
      </li>
      <li>
        <svg class="contact-icon" viewBox="0 0 24 24"><path d="M2 5h20v14H2z M4 7v.5l8 5 8-5V7l-8 5z" fill-rule="evenodd"/></svg>
        daniel@brightwell.com
      </li>
      <li>
        <svg class="contact-icon" viewBox="0 0 24 24"><path d="M12 2a10 10 0 1 0 0 20 10 10 0 0 0 0-20zm6.9 6h-2.9a15 15 0 0 0-1.4-3.6A8 8 0 0 1 18.9 8zM12 4c.8 1.2 1.5 2.5 1.9 4h-3.8c.4-1.5 1.1-2.8 1.9-4zM4.3 14a8 8 0 0 1 0-4h3.4a16 16 0 0 0 0 4zm.8 2h2.9c.3 1.3.8 2.5 1.4 3.6A8 8 0 0 1 5.1 16zM8 8H5.1a8 8 0 0 1 4.3-3.6C8.8 5.5 8.3 6.7 8 8zm4 12c-.8-1.2-1.5-2.5-1.9-4h3.8c-.4 1.5-1.1 2.8-1.9 4zm2.3-6H9.7a14 14 0 0 1 0-4h4.6a14 14 0 0 1 0 4zm.3 5.6c.6-1.1 1.1-2.3 1.4-3.6h2.9a8 8 0 0 1-4.3 3.6zm1.7-5.6a16 16 0 0 0 0-4h3.4a8 8 0 0 1 0 4z"/></svg>
        www.brightwellholdings.com
      </li>
    </ul>

    <div class="brand-lockup">
      <span class="brand-mark" aria-hidden="true"></span>
      <p class="brand-name">Brightwell Holdings</p>
    </div>
  </section>
</main>
</body>
</html>
```